Harbor Tandem Web Design Project

We need a website design for a start up company called "Harbor Tandem". We provide business consultancy services as well as technology-related services (IT). The design should communicate simplicity and elegance. The domain name of the site will be harbortandem.com. The logo of the company is https://files.pinvault.net/u/8147206/7730_2049185_31947_image.jpg
Updates

Target Market(s)

SMB, Corporates, Semi-governments, Governments.

Industry/Entity Type

Business

Requirements
Must have
• - The background of the pages should be white or soft grey, but we are open for suggestions.
- The pages should have nice menu animations.
- The pages should be "portal-style", with multiple placeholders for different sections and multiple tabs.
Nice to have
• The page should auto-fit the screen and scroll vertically as much as needed.
Should not have
• - Flash Animations.
- Generic Photos.

```html
<!DOCTYPE html>
<html lang="en">
<head>
<meta charset="utf-8">
<title>Harbor Tandem</title>
<link href="https://fonts.googleapis.com/css2?family=Open+Sans:ital,wght@0,400;0,600;0,700;1,700&family=Arvo:wght@700&display=swap" rel="stylesheet">
<style>
:root{
  --blue:#1c7fa6;
  --blue-dark:#1f4fa0;
  --sky:#1ab4e8;
  --hero-band-top:#5ec3d8;
  --hero-band-bottom:#2078a8;
  --red:#c0161f;
  --red-btn:#e8380f;
  --green-btn:#1e9a1e;
  --ink:#2b2b2b;
  --panel-dark:#2e2e2e;
  --footer:#343434;
  --footer-bar:#1e1e1e;
  --grey-col:#6b6b6b;
  --body-grey:#dcdbd4;
  --white:#ffffff;
  --dash:#8ab7cf;
}
*{box-sizing:border-box;margin:0;padding:0}
html,body{width:845px;height:1200px;overflow:hidden}
body{position:relative;background:var(--white);font-family:"Open Sans",Arial,sans-serif;color:var(--ink)}
.abs{position:absolute}

/* header */
.brand{left:96px;top:48px;display:flex;align-items:center;gap:10px}
.brand-dot{width:26px;height:26px;border-radius:50%;background:var(--red)}
.brand-name{font-size:27px;font-weight:600;color:var(--blue-dark);letter-spacing:-.3px}
.call-ribbon{left:601px;top:0;width:157px;height:110px}
.call-text{left:601px;top:40px;width:157px;text-align:center;color:var(--white)}
.call-text .big{font-family:"Arvo",Georgia,serif;font-size:21px;line-height:1.1}
.call-text .num{font-size:14px;font-weight:700}

/* hero */
.hero-band{left:0;top:181px;width:845px;height:265px;background:linear-gradient(var(--hero-band-top),var(--hero-band-bottom) 60%,#4aa9cf)}
.nav{left:96px;top:142px;width:662px;height:39px;background:#1e1e1e;border-radius:6px 6px 0 0;display:flex;align-items:center;padding-left:6px;gap:6px}
.nav a{font-size:13px;color:var(--white);text-decoration:none;background:#050505;padding:2px 6px;border-radius:3px}
.nav a.active{background:var(--blue);font-weight:700;position:relative}
.nav a.active::after{content:"";position:absolute;left:50%;bottom:-7px;margin-left:-6px;border:6px solid transparent;border-top-color:var(--blue);border-bottom:0}
.nav .spacer{flex:1}
.nav a.login{background:var(--red-btn);font-weight:700;padding:2px 12px}
.nav a.signup{background:var(--green-btn);font-weight:700;padding:2px 10px;margin-right:16px}
.hero-visual{left:96px;top:181px;width:662px;height:265px;background:linear-gradient(120deg,#6d7479 0%,#c9ccce 28%,#2aa7df 42%,#bfc3c6 60%,#e6e7e8 80%,#8f9496 100%)}
.hero-caption{left:473px;top:285px;width:285px;height:91px;background:rgba(40,40,40,.82);border-radius:14px 0 0 14px;padding:10px 14px 0 24px;color:var(--white)}
.hero-caption p{font-size:15px;font-weight:600;line-height:1.2}
.hero-btn{position:absolute;right:28px;bottom:12px;background:var(--blue);font-size:12px;font-weight:600;padding:1px 4px;border-radius:3px}

/* body */
.body-bg{left:0;top:446px;width:845px;height:455px;background:repeating-linear-gradient(45deg,#d6d5ce 0 2px,#e2e1da 2px 4px)}
.hot-links{left:94px;top:482px;width:177px;height:338px;background:var(--white);border-radius:0 0 8px 8px}
.panel-head{height:22px;background:var(--blue);color:var(--white);font-size:15px;font-weight:600;padding-left:15px;line-height:22px}
.link-list{list-style:none;margin-top:6px}
.link-list li{height:30px;border-bottom:1px dashed var(--dash);display:flex;align-items:center;justify-content:space-between;padding:0 8px 0 15px;font-size:13px}
.link-list li.current{color:var(--blue);font-weight:600}
.arrow-dot{width:16px;height:16px}
.hot-visual{margin:8px 0 0 7px;width:163px;height:116px;background:linear-gradient(135deg,#0e3558,#3d80b0 55%,#0b2d4e)}
.search{left:94px;top:829px;width:177px;height:43px;background:var(--white);padding:8px 0 0 14px}
.search-row{display:flex;align-items:center;gap:8px;font-size:12px;font-weight:700}
.search-field{background:#666;color:var(--white);font-size:9px;font-weight:400;width:80px;padding:1px 14px;border-radius:2px}
.search-sub{font-size:7px;margin-top:3px}

.main{left:283px;top:482px;width:475px;height:390px;background:var(--white);border-radius:0 0 0 6px}
.main-head{height:22px;background:var(--panel-dark);color:var(--white);font-size:15px;font-weight:600;padding-left:16px;line-height:22px}
.article{position:absolute;left:14px;top:36px;width:320px}
.article h2{font-size:14px;font-weight:700;color:var(--blue)}
.article p{font-size:11px;line-height:1.2;margin-top:14px}
.article h2.second{margin-top:18px}
.ticks{list-style:none;margin:8px 0 0 10px}
.ticks li{font-size:11px;display:flex;align-items:center;gap:8px;height:16.5px}
.learn-btn{margin-top:15px;width:115px;height:22px;border:1px solid #ccc;border-radius:3px;background:linear-gradient(#fff,#e6e6e6);font-size:8px;color:#4a6d8c;display:flex;align-items:center;justify-content:space-between;padding:0 6px 0 9px}
.products{position:absolute;left:346px;top:22px;width:129px;height:368px;background:var(--grey-col)}
.products h3{color:var(--white);font-size:14px;font-weight:600;margin:14px 0 0 8px}
.product{position:absolute;left:21px;width:123px;height:79px;background:var(--red);color:var(--white);padding:6px 8px}
.product::before{content:"";position:absolute;right:0;top:-8px;border-left:16px solid transparent;border-bottom:8px solid #111}
.product h4{font-size:13px;font-weight:600}
.product p{font-size:9px;line-height:1.15;margin-top:5px;width:100px}
.product svg{position:absolute;right:16px;bottom:6px}

/* footer */
.footer{left:0;top:901px;width:845px;height:263px;background:var(--footer);border-top:9px solid #4d4d4d}
.foot-title{font-size:14px;font-weight:700;color:var(--sky)}
.testimonial{width:270px;font-size:11px;line-height:1.2;color:var(--white)}
.testimonial cite{display:block;text-align:right;font-size:11px;font-weight:700;font-style:italic;color:var(--sky);margin-top:4px}
.partner{width:96px;height:85px;background:linear-gradient(#e9ecef,#9aa3ab)}
.foot-bar{left:0;top:1164px;width:845px;height:36px;background:var(--footer-bar);display:flex;justify-content:center;align-items:center}
.foot-bar a{color:var(--white);font-size:13px;text-decoration:none;padding:0 9px;border-left:1px solid #777}
.foot-bar a:first-child{border-left:0}
</style>
</head>
<body>

<header>
  <div class="abs brand"><span class="brand-dot"></span><span class="brand-name">Harbor Tandem</span></div>
  <svg class="abs call-ribbon" viewBox="0 0 157 110" aria-hidden="true"><path d="M0 0H157V96L78 110 0 96Z" fill="#c0161f"/></svg>
  <div class="abs call-text"><div class="big">Call us now</div><div class="num">1800 - harbor</div></div>
</header>

<section>
  <div class="abs hero-band"></div>
  <div class="abs hero-visual" role="img" aria-label="Close-up of a keyboard with a blue key carrying a cloud symbol"></div>
  <nav class="abs nav">
    <a class="active" href="#">Home</a><a href="#">About Us</a><a href="#">Our Services</a><a href="#">Our products</a><a href="#">Be Involved</a><a href="#">Contact Us</a>
    <span class="spacer"></span><a class="login" href="#">Login</a><a class="signup" href="#">Sign Up</a>
  </nav>
  <div class="abs hero-caption"><p>Store your company files in our cloud now safer than ever.</p><span class="hero-btn">Learn More</span></div>
</section>

<main>
  <div class="abs body-bg"></div>

  <aside class="abs hot-links">
    <div class="panel-head">Hot Links</div>
    <ul class="link-list">
      <li class="current">Home<svg class="arrow-dot" viewBox="0 0 16 16"><circle cx="8" cy="8" r="8" fill="#2a8bc0"/><path d="M6 4l4 4-4 4" stroke="#fff" stroke-width="2" fill="none"/></svg></li>
      <li>About Us<svg class="arrow-dot" viewBox="0 0 16 16"><circle cx="8" cy="8" r="8" fill="#2a8bc0"/><path d="M6 4l4 4-4 4" stroke="#fff" stroke-width="2" fill="none"/></svg></li>
      <li>Our Services<svg class="arrow-dot" viewBox="0 0 16 16"><circle cx="8" cy="8" r="8" fill="#2a8bc0"/><path d="M6 4l4 4-4 4" stroke="#fff" stroke-width="2" fill="none"/></svg></li>
      <li>Our products<svg class="arrow-dot" viewBox="0 0 16 16"><circle cx="8" cy="8" r="8" fill="#2a8bc0"/><path d="M6 4l4 4-4 4" stroke="#fff" stroke-width="2" fill="none"/></svg></li>
      <li>Be Involved<svg class="arrow-dot" viewBox="0 0 16 16"><circle cx="8" cy="8" r="8" fill="#2a8bc0"/><path d="M6 4l4 4-4 4" stroke="#fff" stroke-width="2" fill="none"/></svg></li>
      <li>Contact Us<svg class="arrow-dot" viewBox="0 0 16 16"><circle cx="8" cy="8" r="8" fill="#2a8bc0"/><path d="M6 4l4 4-4 4" stroke="#fff" stroke-width="2" fill="none"/></svg></li>
    </ul>
    <div class="hot-visual" role="img" aria-label="Illustration of an open hand holding a glowing cloud on a blue background"></div>
  </aside>

  <div class="abs search">
    <div class="search-row">SEARCH<span class="search-field">Search site</span>
      <svg width="16" height="16" viewBox="0 0 16 16"><circle cx="6" cy="6" r="4.5" stroke="#333" stroke-width="2" fill="none"/><path d="M9.5 9.5L15 15" stroke="#333" stroke-width="2.5"/></svg></div>
    <div class="search-sub">Advanced Search | Tips</div>
  </div>

  <section class="abs main">
    <div class="main-head">About Us</div>
    <div class="article">
      <h2>Why to choose harbor tandem</h2>
      <p>Lorem Ipsum is simply dummy text of the printing and typesetting industry. Lorem Ipsum has been the industry's standard dummy text ever since the 1500s, when an unknown printer took a galley of type and scrambled it to make a type specimen book. It has survived not only five centuries, but also the leap into electronic typesetting, remaining essentially unchanged. It was popularised in the 1960s.</p>
      <h2 class="second">Make you life easier with ledgerline</h2>
      <p>Lorem Ipsum is simply dummy text of the printing and typesetting industry. Lorem Ipsum has been the industry's standard dummy text ever since the 1500s.</p>
      <ul class="ticks">
        <li><svg width="14" height="12" viewBox="0 0 14 12"><path d="M1 6l4 4 8-9" stroke="#5a9a1a" stroke-width="3" fill="none"/></svg>When an unknown printer</li>
        <li><svg width="14" height="12" viewBox="0 0 14 12"><path d="M1 6l4 4 8-9" stroke="#5a9a1a" stroke-width="3" fill="none"/></svg>Took a galley of type and scrambled</li>
        <li><svg width="14" height="12" viewBox="0 0 14 12"><path d="M1 6l4 4 8-9" stroke="#5a9a1a" stroke-width="3" fill="none"/></svg>Lorem Ipsum is simply dummy text</li>
        <li><svg width="14" height="12" viewBox="0 0 14 12"><path d="M1 6l4 4 8-9" stroke="#5a9a1a" stroke-width="3" fill="none"/></svg>Of the printing and typesetting</li>
        <li><svg width="14" height="12" viewBox="0 0 14 12"><path d="M1 6l4 4 8-9" stroke="#5a9a1a" stroke-width="3" fill="none"/></svg>Dummy text ever since the 1500s</li>
      </ul>
      <div class="learn-btn">Learn More<svg width="16" height="6" viewBox="0 0 16 6"><path d="M0 3h14M11 0l4 3-4 3" stroke="#4a6d8c" fill="none"/></svg></div>
    </div>

    <div class="products">
      <h3>Our Products</h3>
      <div class="product" style="top:50px"><h4>Product 1</h4><p>Lorem Ipsum is simply dummy text of the printing</p><svg width="16" height="16" viewBox="0 0 16 16"><circle cx="8" cy="8" r="8" fill="#1a1a1a"/><path d="M6 4l4 4-4 4" stroke="#fff" stroke-width="2" fill="none"/></svg></div>
      <div class="product" style="top:153px"><h4>Product 2</h4><p>Lorem Ipsum is simply dummy text of the printing</p><svg width="16" height="16" viewBox="0 0 16 16"><circle cx="8" cy="8" r="8" fill="#1a1a1a"/><path d="M6 4l4 4-4 4" stroke="#fff" stroke-width="2" fill="none"/></svg></div>
      <div class="product" style="top:256px"><h4>Product 3</h4><p>Lorem Ipsum is simply dummy text of the printing</p><svg width="16" height="16" viewBox="0 0 16 16"><circle cx="8" cy="8" r="8" fill="#1a1a1a"/><path d="M6 4l4 4-4 4" stroke="#fff" stroke-width="2" fill="none"/></svg></div>
    </div>
  </section>
</main>

<footer>
  <div class="abs footer"></div>
  <h3 class="abs foot-title" style="left:112px;top:920px">Testimonials</h3>
  <blockquote class="abs testimonial" style="left:111px;top:957px">Lorem Ipsum is simply dummy text of the printing and typesetting industry. Lorem Ipsum has been the industry's standard dummy text ever since the 1500s.<cite>Delia R.</cite></blockquote>
  <blockquote class="abs testimonial" style="left:111px;top:1042px">Lorem Ipsum is simply dummy text of the printing and typesetting industry. Lorem Ipsum has been the industry's standard dummy text ever since the 1500s.<cite>Marcus T.</cite></blockquote>
  <h3 class="abs foot-title" style="left:449px;top:920px">Partners</h3>
  <div class="abs partner" style="left:436px;top:960px" role="img" aria-label="Partner photo: businessman on the phone"></div>
  <div class="abs partner" style="left:544px;top:960px" role="img" aria-label="Partner photo: businessman on the phone"></div>
  <div class="abs partner" style="left:649px;top:960px" role="img" aria-label="Partner photo: smiling businessman with team"></div>
  <div class="abs partner" style="left:436px;top:1055px" role="img" aria-label="Partner photo: team giving thumbs up"></div>
  <div class="abs partner" style="left:544px;top:1055px" role="img" aria-label="Partner photo: team giving thumbs up"></div>
  <div class="abs partner" style="left:649px;top:1055px" role="img" aria-label="Partner photo: support agent with headset"></div>
  <nav class="abs foot-bar"><a href="#">Home</a><a href="#">About Us</a><a href="#">Our Services</a><a href="#">Our products</a><a href="#">Be Involved</a><a href="#">Contact Us</a></nav>
</footer>

</body>
</html>
```